Stationery and Business Card Design

We need stationary design for our new company pelvanta. Pelvanta is a company that provides city apartment rentals for tourists in Athens We need business cards, letterheads for A4 and A5 and envelopes for A4 A5. The design needs to be modern, friendly and corporate.

Target Market(s)

City Tourists

Industry/Entity Type

Tourism

```html
<!DOCTYPE html>
<html lang="en">
<head>
<meta charset="utf-8">
<title>Pelvanta Apartments – Letterhead and Envelope Set</title>
<link href="https://fonts.googleapis.com/css2?family=Raleway:wght@300;400&display=swap" rel="stylesheet">
<style>
  :root {
    --backdrop: #d4d4d6;
    --paper: #f5f5f5;
    --brand-plum: #7b1d52;
    --brand-charcoal: #3e3e3e;
    --ink: #4a4a4a;
  }
  * { margin: 0; padding: 0; box-sizing: border-box; }
  html, body { width: 1200px; height: 991px; overflow: hidden; }
  body {
    position: relative;
    background: var(--backdrop);
    font-family: "Raleway", sans-serif;
  }
  .sheet, .envelope { position: absolute; background: var(--paper); }
  .envelope svg { position: absolute; inset: 0; }

  .footer-band { position: absolute; left: 0; right: 0; bottom: 0; display: flex; }
  .footer-band .band-dark { background: var(--brand-charcoal); }
  .footer-band .band-plum { background: var(--brand-plum); flex: 1; }

  .brand { position: absolute; display: flex; flex-direction: column; align-items: center; }
  .brand-square { background: var(--brand-plum); }
  .brand-name { color: var(--brand-plum); font-weight: 400; line-height: 1; }
  .brand-tagline {
    display: flex; align-items: center; color: var(--brand-plum);
    font-weight: 400; text-transform: uppercase;
  }
  .brand-tagline::before, .brand-tagline::after {
    content: ""; display: block; height: 1px; background: #9a8a92;
  }
  .brand-address { color: var(--ink); text-align: center; font-weight: 400; }

  /* A4 set */
  .envelope--a4 { left: 366px; top: 130px; width: 577px; height: 408px; }
  .sheet--a4 { left: 257px; top: 78px; width: 576px; height: 406px; }
  .sheet--a4 .footer-band { height: 11px; }
  .sheet--a4 .band-dark { width: 227px; }
  .sheet--a4 .brand { left: 26px; top: 40px; width: 140px; }
  .sheet--a4 .brand-square { width: 36px; height: 36px; margin-bottom: 6px; }
  .sheet--a4 .brand-name { font-size: 26px; }
  .sheet--a4 .brand-tagline { font-size: 6.5px; letter-spacing: 2.6px; margin-top: 2px; gap: 5px; }
  .sheet--a4 .brand-tagline::before, .sheet--a4 .brand-tagline::after { width: 20px; }
  .sheet--a4 .brand-address { font-size: 6px; line-height: 8px; margin-top: 14px; }

  /* A5 set */
  .envelope--a5 { left: 446px; top: 630px; width: 403px; height: 283px; }
  .sheet--a5 { left: 350px; top: 583px; width: 407px; height: 287px; }
  .sheet--a5 .footer-band { height: 8px; }
  .sheet--a5 .band-dark { width: 160px; }
  .sheet--a5 .brand { left: 20px; top: 29px; width: 106px; }
  .sheet--a5 .brand-square { width: 25px; height: 25px; margin-bottom: 4px; }
  .sheet--a5 .brand-name { font-size: 18px; }
  .sheet--a5 .brand-tagline { font-size: 4.5px; letter-spacing: 1.8px; margin-top: 1px; gap: 4px; }
  .sheet--a5 .brand-tagline::before, .sheet--a5 .brand-tagline::after { width: 16px; }
  .sheet--a5 .brand-address { font-size: 4.5px; line-height: 6px; margin-top: 9px; }
</style>
</head>
<body>

  <!-- A4 envelope -->
  <div class="envelope envelope--a4">
    <svg width="577" height="408" viewBox="0 0 577 408" aria-hidden="true">
      <polygon points="518,18 577,0 577,408 518,390" fill="var(--brand-plum)"/>
      <rect x="536" y="193" width="24" height="24" fill="#ffffff"/>
    </svg>
  </div>

  <!-- A4 letterhead -->
  <div class="sheet sheet--a4">
    <div class="brand">
      <div class="brand-square"></div>
      <div class="brand-name">Pelvanta</div>
      <div class="brand-tagline">Apartments</div>
      <div class="brand-address">14 Ermou Street<br>Athens, GR, 10563</div>
    </div>
    <div class="footer-band"><div class="band-dark"></div><div class="band-plum"></div></div>
  </div>

  <!-- A5 envelope -->
  <div class="envelope envelope--a5">
    <svg width="403" height="283" viewBox="0 0 403 283" aria-hidden="true">
      <polygon points="362,10 403,0 403,283 362,273" fill="var(--brand-plum)"/>
      <rect x="374" y="133" width="16" height="17" fill="#ffffff"/>
    </svg>
  </div>

  <!-- A5 letterhead -->
  <div class="sheet sheet--a5">
    <div class="brand">
      <div class="brand-square"></div>
      <div class="brand-name">Pelvanta</div>
      <div class="brand-tagline">Apartments</div>
      <div class="brand-address">14 Ermou Street<br>Athens, GR, 10563</div>
    </div>
    <div class="footer-band"><div class="band-dark"></div><div class="band-plum"></div></div>
  </div>

</body>
</html>
```